Progressive Architecture and Urban Planning Studio - Stationery Design

The Kestrel Collective: a small boutique Architectural and Urban Planning Studio based in Natal/ RN, Brazil, about to open branches in South Africa and West Africa, established to provide high quality, innovative design and personal client service for projects worldwide. Our approach to Architecture: Minimal - Less is More, so to speak, but with an edge! Strive to produce "clean" projects - stripped of all that can be stripped, no excesses. Got our Logo right here with Pixel Harbor, and hope to do the same with our stationery (were informed that includes business cards, letterhead and envelopes). Since we'll be using two clour schemes, we want at least one using a black background (business card). We'll also allow manipulation of our logo if it helps the final design. Good Luck!

Industry/Entity Type

Business

Other font styles liked:
• Nexa

Colors

Designer to choose colors to be used in the design.

Requirements
Must have
• Business Cards/ Letterheads with the following address:
Rua Benedito Sarmento 742, Jardim Aurora, Vila Clara/RN
Should be able to edit it.

```html
<!DOCTYPE html>
<html lang="en">
<head>
<meta charset="utf-8">
<title>The Kestrel Collective – Stationery</title>
<link rel="stylesheet" href="https://fonts.googleapis.com/css2?family=Montserrat:wght@600&family=Questrial&family=PT+Sans+Narrow:wght@400;700&display=swap">
<style>
  :root {
    --backdrop: #d9dbdd;
    --paper: #ffffff;
    --ink: #222222;
    --ink-soft: #444444;
    --red: #ee1c1c;
    --red-deep: #a50d0d;
    --card-black: #050505;
    --fold-line: #c9c9c9;
  }
  * { box-sizing: border-box; margin: 0; padding: 0; }
  html, body { width: 1200px; height: 848px; overflow: hidden; }
  body { background: var(--backdrop); position: relative; font-family: "PT Sans Narrow", sans-serif; color: var(--ink); }

  .sheet { position: absolute; background: var(--paper); overflow: hidden; }
  .sheet--dark { background: var(--card-black); }

  .band { position: absolute; left: 0; right: 0; height: 14px;
    background: linear-gradient(90deg, var(--red-deep) 0%, var(--red) 18%, var(--red) 75%, var(--red-deep) 100%); }
  .band--top { top: 0; clip-path: polygon(0 0, 100% 0, 100% 60%, 20% 60%, 19% 100%, 0 100%); }
  .band--bottom { bottom: 0; clip-path: polygon(0 0, 20% 40%, 100% 40%, 100% 100%, 0 100%); }

  .brand { position: absolute; display: flex; align-items: center; gap: 9px;
    font-family: "Montserrat", sans-serif; font-weight: 600; letter-spacing: 0.2em;
    text-transform: uppercase; white-space: nowrap; color: var(--ink); }
  .brand__square { width: 22px; height: 22px; background: var(--red); flex: none; }
  .brand--light { color: #ffffff; }
  .brand--light .brand__square { background: #ffffff; width: 14px; height: 14px; }

  .address { position: absolute; font-size: 9.5px; color: var(--ink-soft); white-space: nowrap; }
  .address b { color: var(--red); font-weight: 700; }

  /* Letterhead */
  .letterhead { left: 28px; top: 34px; width: 552px; height: 778px; }
  .letterhead .brand { right: 28px; top: 24px; font-size: 11.5px; }
  .letterhead .address { right: 22px; bottom: 18px; }

  /* Business card front */
  .card-front { left: 603px; top: 34px; width: 270px; height: 165px; }
  .card-front .brand { left: 42px; top: 19px; font-size: 8.5px; letter-spacing: 0.14em; gap: 8px; }
  .card-front .brand__square { width: 17px; height: 17px; }
  .card-front__role { position: absolute; left: 0; right: 0; top: 48px; text-align: center;
    font-family: "Questrial", sans-serif; font-size: 20px; color: var(--ink); }
  .card-front__title { position: absolute; right: 70px; top: 72px;
    font-family: "Questrial", sans-serif; font-size: 10px; font-style: italic; color: var(--ink-soft); }
  .card-front .address { left: 0; right: 0; text-align: center; font-size: 9px; }
  .card-front .address--street { top: 113px; }
  .card-front .address--phone { top: 127px; }
  .card-front .band, .card-back .band { height: 12px; }

  /* Business card back */
  .card-back { left: 893px; top: 34px; width: 270px; height: 165px; }
  .card-back .brand { left: 0; right: 0; justify-content: center; top: 77px; font-size: 8px; letter-spacing: 0.16em; gap: 8px; }

  /* Envelope front */
  .dl-sheet { left: 613px; top: 248px; width: 545px; height: 274px; }
  .dl-sheet .brand { left: 15px; top: 19px; font-size: 9.5px; letter-spacing: 0.15em; }
  .dl-sheet .brand__square { width: 20px; height: 20px; }
  .dl-sheet .address { left: 46px; top: 48px; font-size: 9px; }
  .dl-sheet .band { height: 12px; }

  /* Envelope back */
  .envelope { left: 613px; top: 540px; width: 545px; height: 272px; }
  .envelope__flap { position: absolute; left: 0; top: 0; width: 545px; height: 100px; }
  .envelope__square { position: absolute; left: 257px; top: 41px; width: 30px; height: 25px; background: var(--red); }
  .envelope__web { position: absolute; left: 0; right: 0; top: 72px; text-align: center;
    font-size: 10px; font-weight: 700; color: var(--ink); }
  .envelope .band { height: 10px; }
</style>
</head>
<body>

  <section class="sheet letterhead" aria-label="Letterhead">
    <div class="band band--top"></div>
    <div class="brand"><span class="brand__square"></span>The Kestrel Collective</div>
    <p class="address">Rua Benedito Sarmento 742, Jardim Aurora, Vila Clara/RN &nbsp;<b>T</b> 00 000 0000 &nbsp;<b>F</b> 00 000 0000</p>
    <div class="band band--bottom"></div>
  </section>

  <section class="sheet card-front" aria-label="Business card, front">
    <div class="brand"><span class="brand__square"></span>The Kestrel Collective</div>
    <p class="card-front__role">Project Owner</p>
    <p class="card-front__title">director</p>
    <p class="address address--street">Rua Benedito Sarmento 742, Jardim Aurora, Vila Clara/RN</p>
    <p class="address address--phone"><b>T</b> 00 000 0000 &nbsp;<b>F</b> 00 000 0000</p>
    <div class="band band--bottom"></div>
  </section>

  <section class="sheet sheet--dark card-back" aria-label="Business card, back">
    <div class="brand brand--light"><span class="brand__square"></span>The Kestrel Collective</div>
    <div class="band band--bottom"></div>
  </section>

  <section class="sheet dl-sheet" aria-label="Envelope, front">
    <div class="brand"><span class="brand__square"></span>The Kestrel Collective</div>
    <p class="address">Rua Benedito Sarmento 742, Jardim Aurora, Vila Clara/RN</p>
    <div class="band band--bottom"></div>
  </section>

  <section class="sheet envelope" aria-label="Envelope, back">
    <svg class="envelope__flap" viewBox="0 0 545 100" aria-hidden="true">
      <path d="M2 2 Q8 84 40 90 L505 90 Q537 84 543 2" fill="none" stroke="var(--fold-line)" stroke-width="1.5"/>
    </svg>
    <span class="envelope__square"></span>
    <p class="envelope__web">www.kestrelcollective.com</p>
    <div class="band band--bottom"></div>
  </section>

</body>
</html>
```